Wordpress Design Project - App Review

Take a look at this website, kivomart.example. We are creating something very similar to this, four pages are required. The name of our website is GlimmerNestHub.example
1) The home page which highlights, Pick of the Day, a carousel which highlights featured apps, and top apps in different categories
2) Single App Page - This page will details the app that is selected, app icon, app description, app ratings, and other information you can find on an app page in the Vortiq bazaar
3) A page that list all the apps in a category, for example if the user select, "100 top apps" the page that will display the list of 100 apps, 10 per page, summary of description, a small icon, screenshot etc for each app
4) Review Page - where we review an Pick of the Day, including screenshots, videos, text reviews etc
I do not have any logo at the moment, use these as nav links; home, my apps, reviews, blog and contact. Thank you.
I will like to see a nice creativity. I am open to a very beautiful color combinations. Thank you
App shoppers, people that are looking for new apps, discounted apps etc
Store

```html
<!DOCTYPE html>
<html lang="en">
<head>
<meta charset="utf-8">
<title>GlimmerNestHub – Top Popular Apps</title>
<link href="https://fonts.googleapis.com/css2?family=Open+Sans:wght@300;400;600;700&display=swap" rel="stylesheet">
<style>
:root{
  --blue:#2391e0;
  --blue-dark:#1a7dc6;
  --orange:#f0962a;
  --orange-dark:#d97d14;
  --grey-bar:#ececec;
  --line:#e2e2e2;
  --text:#555;
  --title:#222;
  --green:#2a8a2a;
  --red:#d9221c;
}
*{box-sizing:border-box;margin:0;padding:0}
html,body{width:750px;height:1200px;overflow:hidden}
body{font-family:'Open Sans',sans-serif;background:#fff;position:relative;color:var(--text)}
.site-header{position:absolute;left:0;top:0;width:750px;height:58px;background:#fff}
.brand{position:absolute;left:113px;top:18px;display:flex;align-items:center;gap:6px}
.brand-dot{width:16px;height:16px;border-radius:50%;background:var(--orange)}
.brand-name{font-size:19px;font-weight:700;color:var(--blue);letter-spacing:-.3px}
.account{position:absolute;right:156px;top:11px;font-size:7.5px;color:#666}
.main-nav{position:absolute;left:430px;top:36px;height:21px;display:flex;background:var(--orange);border-radius:3px 3px 0 0}
.main-nav a{color:#fff;font-size:8.5px;font-weight:700;text-decoration:none;padding:0 8px;line-height:21px;border-right:1px solid var(--orange-dark)}
.main-nav a:last-child{border-right:0}
.filter-bar{position:absolute;left:0;top:58px;width:750px;height:36px;background:var(--grey-bar);border-top:1px solid #ddd}
.seg{position:absolute;top:8px;height:18px;display:flex;border:1px solid #c8c8c8;border-radius:2px;background:#f5f5f5;overflow:hidden}
.seg span{font-size:6.5px;font-weight:600;color:#444;padding:0 4px;line-height:16px;border-right:1px solid #d0d0d0}
.seg span:last-child{border-right:0}
.seg .on{background:var(--blue);color:#fff}
.select{position:absolute;left:232px;top:8px;width:104px;height:18px;border:1px solid #c8c8c8;background:#f5f5f5;font-size:6.5px;line-height:16px;padding-left:5px;color:#444}
.select i{position:absolute;right:0;top:0;width:15px;height:16px;background:#ddd}
.select i:after{content:"";position:absolute;left:4px;top:6px;border:3.5px solid transparent;border-top:4px solid #666}
.search{position:absolute;left:530px;top:8px;width:107px;height:18px;border:1px solid #c8c8c8;background:#f5f5f5;font-size:7px;line-height:16px;padding-left:6px;color:#666}
.search i{position:absolute;right:0;top:0;width:19px;height:16px;background:#ddd}
.blue-band{position:absolute;left:0;top:94px;width:750px;height:210px;background:var(--blue)}
.page-title{position:absolute;left:113px;top:104px;font-size:23px;font-weight:300;color:#fff}
.app-list{position:absolute;left:112px;top:137px;width:526px;height:1005px;background:#fff;border:1px solid #ddd;border-radius:4px}
.app{position:absolute;left:13px;width:499px;height:97px}
.app .sep{position:absolute;left:0;top:81px;width:499px;height:1px;background:var(--line)}
.icon{position:absolute;left:1px;top:0;width:56px;height:56px;border:1px solid #ccc;border-radius:6px;padding:3px;background:#fff}
.icon .art{width:100%;height:100%;border-radius:4px}
.icon .badge{position:absolute;left:4px;top:4px;width:8px;height:8px;font-size:6px;font-weight:700;color:#fff;text-align:center;line-height:8px}
.badge.free{background:#2f9c2f}.badge.paid{background:#d42a1f}
.status{position:absolute;left:0;top:65px;font-size:7.5px;display:flex;align-items:center;gap:3px}
.status.drop{color:var(--green)}.status.new{color:var(--blue)}.status.up{color:var(--red)}
.info{position:absolute;left:69px;top:4px;width:325px}
.info h3{font-size:8.8px;font-weight:600;color:var(--title)}
.meta{font-size:7px;margin-top:2px;color:var(--orange)}
.meta b{font-weight:600;color:var(--blue)}
.desc{font-size:6.9px;line-height:13px;margin-top:1px;color:#666}
.pricing{position:absolute;left:401px;top:6px;width:97px;text-align:center}
.price{font-size:10px;font-weight:700;color:var(--blue);height:14px}
.price s{color:#444;margin-right:8px}
.get{display:block;margin-top:4px;height:19px;background:var(--orange);border-radius:3px;color:#fff;font-size:9.5px;font-weight:700;line-height:19px;letter-spacing:.6px}
.save{margin-top:6px;font-size:6px;font-weight:700;color:var(--blue);white-space:nowrap}
.pager{position:absolute;left:0;top:1116px;width:750px;display:flex;justify-content:center;gap:2px}
.pager span{min-width:13px;height:11px;padding:0 2px;border:1px solid #ccc;font-size:6px;line-height:9px;text-align:center;color:#555}
.pager .on{background:#666;color:#fff;border-color:#666}
.site-footer{position:absolute;left:0;top:1157px;width:750px;height:43px;background:var(--blue);color:#fff;font-size:7.5px}
.foot-nav{position:absolute;left:117px;top:15px;display:flex;gap:9px}
.copy{position:absolute;right:116px;top:15px}
</style>
</head>
<body>
<header class="site-header">
  <div class="brand"><span class="brand-dot"></span><span class="brand-name">GlimmerNestHub</span></div>
  <div class="account">Login &nbsp;|&nbsp; Register</div>
  <nav class="main-nav"><a>HOME</a><a>MY APPS</a><a>REVIEWS</a><a>CONTACT</a></nav>
</header>

<div class="filter-bar">
  <div class="seg" style="left:117px"><span class="on">All</span><span>Phone</span><span>Tablet</span><span>Universal</span></div>
  <div class="select">All Categories<i></i></div>
  <div class="seg" style="left:341px"><span class="on">All</span><span>Paid</span><span>Free</span></div>
  <div class="seg" style="left:407px"><span class="on">All</span><span>Updates</span><span>New</span><span>Price Drops</span></div>
  <div class="search">Search App<i><svg width="19" height="16" viewBox="0 0 19 16"><circle cx="9" cy="7" r="3.2" fill="none" stroke="#666" stroke-width="1.4"/><line x1="11.3" y1="9.3" x2="14" y2="12" stroke="#666" stroke-width="1.6"/></svg></i></div>
</div>

<div class="blue-band"></div>
<h1 class="page-title">TOP POPULAR APPS</h1>

<main class="app-list">
  <article class="app" style="top:16px">
    <div class="icon"><div class="art" role="img" aria-label="Racing minibus icon" style="background:linear-gradient(160deg,#c63b2c,#e8c24a 55%,#3b3b3b)"></div><span class="badge free">F</span></div>
    <div class="status drop"><svg width="8" height="8" viewBox="0 0 8 8"><circle cx="4" cy="4" r="4" fill="#2a8a2a"/><path d="M4 1.8v4M2.3 4.3L4 6l1.7-1.7" stroke="#fff" fill="none" stroke-width="1"/></svg>Price Drop</div>
    <div class="info"><h3>RoutePal Contacts Sync</h3><div class="meta"><b>Featured:</b> &nbsp;2 hours ago &nbsp;| &nbsp;<b>Rating:</b> &nbsp;No data &nbsp;| &nbsp;<b>Version:</b> &nbsp;1.0 &nbsp;Mobile Universal</div><p class="desc">Minibus Rider is a car racing game set in a busy harbour town. "This Game is absurdly addictive and fun!" A minibus is a kind of shared taxi. These vehicles have routes without timetables, but...</p></div>
    <div class="pricing"><div class="price"><s>1.50</s>FREE</div><a class="get">GET THE APP</a><div class="save">Save this App | I have this app</div></div>
    <div class="sep"></div>
  </article>

  <article class="app" style="top:113px">
    <div class="icon"><div class="art" role="img" aria-label="Photo transfer icon" style="background:linear-gradient(180deg,#f39a1e,#f6c04a 50%,#3aa3e0)"></div><span class="badge free">F</span></div>
    <div class="status drop"><svg width="8" height="8" viewBox="0 0 8 8"><circle cx="4" cy="4" r="4" fill="#2a8a2a"/><path d="M4 1.8v4M2.3 4.3L4 6l1.7-1.7" stroke="#fff" fill="none" stroke-width="1"/></svg>Price Drop</div>
    <div class="info"><h3>Snapwave Transfer - video...</h3><div class="meta"><b>Featured:</b> &nbsp;2 hours ago &nbsp;| &nbsp;<b>Rating:</b> &nbsp;No data &nbsp;| &nbsp;<b>Version:</b> &nbsp;1.0 &nbsp;Mobile Universal</div><p class="desc">Featured in DailyFreeApps. Your daily free app resource. Snapwave Transfer is the easiest and fastest way to send and receive photos and videos from/to your tablet, phone, player and computer over...</p></div>
    <div class="pricing"><div class="price"><s>0.99</s>FREE</div><a class="get">GET THE APP</a><div class="save">Save this App | I have this app</div></div>
    <div class="sep"></div>
  </article>

  <article class="app" style="top:210px">
    <div class="icon"><div class="art" role="img" aria-label="Fighter plane game icon" style="background:linear-gradient(180deg,#8fb64a,#c8342a 50%,#4f7a2e)"></div><span class="badge paid">P</span></div>
    <div class="status new"><svg width="8" height="8" viewBox="0 0 8 8"><path d="M0 0h4l4 4-4 4-4-4z" fill="#2391e0"/><circle cx="2" cy="2" r=".8" fill="#fff"/></svg>New</div>
    <div class="info"><h3>Skyhawk Fighter Reloaded</h3><div class="meta"><b>Featured:</b> &nbsp;2 hours ago &nbsp;| &nbsp;<b>Rating:</b> &nbsp;No data &nbsp;| &nbsp;<b>Version:</b> &nbsp;1.0 &nbsp;Mobile Universal</div><p class="desc">Download the FreshPickADay App and wish for more top rated paid apps like Skyhawk Fighter Reloaded to become FREE for a day! This is the ultimate classic arcade style shooter! ...</p></div>
    <div class="pricing"><div class="price">1.29</div><a class="get">GET THE APP</a><div class="save">Save this App | I have this app</div></div>
    <div class="sep"></div>
  </article>

  <article class="app" style="top:307px">
    <div class="icon"><div class="art" role="img" aria-label="Space adventure game icon" style="background:linear-gradient(160deg,#3a4a5a,#8a5a3a 55%,#1f2a33)"></div><span class="badge paid">P</span></div>
    <div class="status up"><svg width="8" height="8" viewBox="0 0 8 8"><circle cx="4" cy="4" r="4" fill="#d9221c"/><path d="M4 6.2v-4M2.3 3.7L4 2l1.7 1.7" stroke="#fff" fill="none" stroke-width="1"/></svg>Price Increase</div>
    <div class="info"><h3>Nebula Hunter Vela</h3><div class="meta"><b>Featured:</b> &nbsp;2 hours ago &nbsp;| &nbsp;<b>Rating:</b> &nbsp;No data &nbsp;| &nbsp;<b>Version:</b> &nbsp;1.0 &nbsp;Mobile Universal</div><p class="desc">A new legend begins! Venture forth to the most immersive world of galaxy wars! Resist the invasion of the empire! You've been tasked to protect several planets. Enjoy the battle! FEATURES -...</p></div>
    <div class="pricing"><div class="price">4.55</div><a class="get">GET THE APP</a><div class="save">Save this App | I have this app</div></div>
    <div class="sep"></div>
  </article>

  <article class="app" style="top:404px">
    <div class="icon"><div class="art" role="img" aria-label="Colourful photo editor icon" style="background:conic-gradient(#e63b2e,#f5b02a,#7cc343,#2a9ad8,#8a3fb5,#e63b2e)"></div><span class="badge free">F</span></div>
    <div class="status new"><svg width="8" height="8" viewBox="0 0 8 8"><path d="M0 0h4l4 4-4 4-4-4z" fill="#2391e0"/><circle cx="2" cy="2" r=".8" fill="#fff"/></svg>New</div>
    <div class="info"><h3>Prismly Photo Editor</h3><div class="meta"><b>Featured:</b> &nbsp;2 hours ago &nbsp;| &nbsp;<b>Rating:</b> &nbsp;No data &nbsp;| &nbsp;<b>Version:</b> &nbsp;1.0 &nbsp;Mobile Universal</div><p class="desc">Prismly Photo Editor is one of the best and easy-to-use photo editing software. With it, you can make your favorite picture by few steps. Its unique editing photo, collaging picture frames and...</p></div>
    <div class="pricing"><div class="price">FREE</div><a class="get">GET THE APP</a><div class="save">Save this App | I have this app</div></div>
    <div class="sep"></div>
  </article>

  <article class="app" style="top:501px">
    <div class="icon"><div class="art" role="img" aria-label="Camera lens location icon" style="background:radial-gradient(circle,#7be0f0 10%,#7a3fa8 35%,#2a2a2a 60%)"></div><span class="badge free">F</span></div>
    <div class="status new"><svg width="8" height="8" viewBox="0 0 8 8"><path d="M0 0h4l4 4-4 4-4-4z" fill="#2391e0"/><circle cx="2" cy="2" r=".8" fill="#fff"/></svg>New</div>
    <div class="info"><h3>LensSpot</h3><div class="meta"><b>Featured:</b> &nbsp;2 hours ago &nbsp;| &nbsp;<b>Rating:</b> &nbsp;No data &nbsp;| &nbsp;<b>Version:</b> &nbsp;1.0 &nbsp;Mobile Universal</div><p class="desc">*** Free today with Pick of the Day *** download the app "Pick of the Day" and discover every day a paid app that becomes free for 24 hours! A location based Photo App to let everyone know...</p></div>
    <div class="pricing"><div class="price">0.99</div><a class="get">GET THE APP</a><div class="save">Save this App | I have this app</div></div>
    <div class="sep"></div>
  </article>

  <article class="app" style="top:598px">
    <div class="icon"><div class="art" role="img" aria-label="Paint palette icon" style="background:linear-gradient(160deg,#3a6fd0,#f2f2f2 45%,#e0c27a)"></div><span class="badge free">F</span></div>
    <div class="status drop"><svg width="8" height="8" viewBox="0 0 8 8"><circle cx="4" cy="4" r="4" fill="#2a8a2a"/><path d="M4 1.8v4M2.3 4.3L4 6l1.7-1.7" stroke="#fff" fill="none" stroke-width="1"/></svg>Price Drop</div>
    <div class="info"><h3>Palette Paint - dabPaint</h3><div class="meta"><b>Featured:</b> &nbsp;2 hours ago &nbsp;| &nbsp;<b>Rating:</b> &nbsp;No data &nbsp;| &nbsp;<b>Version:</b> &nbsp;1.0 &nbsp;Mobile Universal</div><p class="desc">Palette Paint - dabPaint is FREE for a limited time | Brought to you by 3 Lucky Picks. Download 3 Lucky Picks to get more awesome apps like Palette Paint - dabPaint for FREE Social painting app...</p></div>
    <div class="pricing"><div class="price"><s>0.45</s>FREE</div><a class="get">GET THE APP</a><div class="save">Save this App | I have this app</div></div>
    <div class="sep"></div>
  </article>

  <article class="app" style="top:695px">
    <div class="icon"><div class="art" role="img" aria-label="Arcade game icon" style="background:linear-gradient(160deg,#5a3fb0,#3fb07a 50%,#e07a3a)"></div><span class="badge free">F</span></div>
    <div class="status up"><svg width="8" height="8" viewBox="0 0 8 8"><circle cx="4" cy="4" r="4" fill="#d9221c"/><path d="M4 6.2v-4M2.3 3.7L4 2l1.7 1.7" stroke="#fff" fill="none" stroke-width="1"/></svg>Price Increase</div>
    <div class="info"><h3>RoutePal Contacts Sync</h3><div class="meta"><b>Featured:</b> &nbsp;2 hours ago &nbsp;| &nbsp;<b>Rating:</b> &nbsp;No data &nbsp;| &nbsp;<b>Version:</b> &nbsp;1.0 &nbsp;Mobile Universal</div><p class="desc">Rushblast 2 HD is FREE for a limited time | Brought to you by 3 Lucky Picks. Download 3 Lucky Picks to get more awesome apps like Rushblast 2 HD for FREE. From the makers of the award winning Math...</p></div>
    <div class="pricing"><div class="price">4.50</div><a class="get">GET THE APP</a><div class="save">Save this App | I have this app</div></div>
    <div class="sep"></div>
  </article>

  <article class="app" style="top:792px">
    <div class="icon"><div class="art" role="img" aria-label="Planet astronomy icon" style="background:radial-gradient(circle at 45% 45%,#5a9ad0,#2a5a8a 45%,#0c1420 70%)"></div><span class="badge paid">P</span></div>
    <div class="status up"><svg width="8" height="8" viewBox="0 0 8 8"><circle cx="4" cy="4" r="4" fill="#d9221c"/><path d="M4 6.2v-4M2.3 3.7L4 2l1.7 1.7" stroke="#fff" fill="none" stroke-width="1"/></svg>Price Increase</div>
    <div class="info"><h3>StarVoyager 3</h3><div class="meta"><b>Featured:</b> &nbsp;2 hours ago &nbsp;| &nbsp;<b>Rating:</b> &nbsp;No data &nbsp;| &nbsp;<b>Version:</b> &nbsp;1.0 &nbsp;Mobile Universal</div><p class="desc">FREE FOR SATURN - THRU JULY 21st! STARGAZER MONTHLY 2012 TOP PICK! TECHWORLD 2010 BEST IN CLASS! As Earth "Smiles at Saturn" on July 19th, use StarVoyager 3 to find the Ringed...</p></div>
    <div class="pricing"><div class="price">3.00</div><a class="get">GET THE APP</a><div class="save">Save this App | I have this app</div></div>
    <div class="sep"></div>
  </article>

  <article class="app" style="top:889px">
    <div class="icon"><div class="art" role="img" aria-label="Digital alarm clock icon" style="background:linear-gradient(180deg,#1a2a3a,#1f5a8a 55%,#0e1a24)"></div><span class="badge free">F</span></div>
    <div class="status drop"><svg width="8" height="8" viewBox="0 0 8 8"><circle cx="4" cy="4" r="4" fill="#2a8a2a"/><path d="M4 1.8v4M2.3 4.3L4 6l1.7-1.7" stroke="#fff" fill="none" stroke-width="1"/></svg>Price Drop</div>
    <div class="info"><h3>Wakeup Clock Master Pro</h3><div class="meta"><b>Featured:</b> &nbsp;2 hours ago &nbsp;| &nbsp;<b>Rating:</b> &nbsp;No data &nbsp;| &nbsp;<b>Version:</b> &nbsp;1.0 &nbsp;Mobile Universal</div><p class="desc">* * * * * The new Desk Remote has been released.It's a universal version for phone and tablet.Try it,maybe it is just your need. * * * * * This APP is not only an Alarm Clock, but also...</p></div>
    <div class="pricing"><div class="price"><s>0.35</s>FREE</div><a class="get">GET THE APP</a><div class="save">Save this App | I have this app</div></div>
    <div class="sep"></div>
  </article>
</main>

<nav class="pager"><span>&lt;&lt;</span><span>&lt;</span><span>1</span><span>2</span><span>3</span><span class="on">4</span><span>5</span><span>&gt;</span><span>&gt;&gt;</span></nav>

<footer class="site-footer">
  <div class="foot-nav"><span>Home</span><span>My Apps</span><span>Reviews</span><span>Contact</span></div>
  <div class="copy">Copyright © 2013 GlimmerNestHub. All rights reserved</div>
</footer>
</body>
</html>
```